Brivolta ERP Campaign Newsletter

Purpose of Document: Professional consulting firm looking to provide prospects with information about our ERP offerings and how we can support them with their ERP implementations. Often we have prospects that are in the middle of implementation and decide they need support.
What are we looking for: Professional look. Please use the attached ERP V5 document brochure content. We are looking for new graphics and layout that makes the content pop. Below is our website and attached company color skus. We want to keep our theme/colors consistent with the website.
Website: https://brivoltaconsulting.com/

Target Market(s)

Target prospects in industries including manufacturing and distribution, supply chain and logistics, and professional services.

Industry/Entity Type

Consulting

Requirements
Must have
• Visual graphics

```html
<!DOCTYPE html>
<html lang="en">
<head>
<meta charset="utf-8">
<title>Brivolta ERP Newsletter</title>
<link href="https://fonts.googleapis.com/css2?family=Poppins:wght@300;400;500;600&display=swap" rel="stylesheet">
<style>
:root{
  --navy:#0d2346;
  --navy-deep:#081832;
  --blue:#2c6cb0;
  --heading-blue:#2f6fae;
  --yellow:#f5c518;
  --grey-photo:#45484e;
  --text:#2a2a2a;
  --white:#ffffff;
  --tech-bg:#f3f5f8;
}
*{margin:0;padding:0;box-sizing:border-box}
html,body{width:1200px;height:5312px;overflow:hidden}
body{font-family:'Poppins',sans-serif;color:var(--text);background:var(--white);position:relative}
section,footer,header{position:absolute;left:0;width:1200px}

.hero{top:0;height:538px;background:radial-gradient(ellipse at 50% 30%,#1f4f96 0%,#10306a 45%,#081a3e 100%)}
.brand{position:absolute;left:0;width:100%;text-align:center;font-weight:500;letter-spacing:2px}
.hero .brand{top:120px;font-size:150px;line-height:1;color:#d9dde4}
.tagline{position:absolute;top:348px;width:100%;text-align:center;font-size:50px;color:var(--yellow);font-weight:400}

.intro{top:538px;height:918px;background:linear-gradient(180deg,#55585e 0%,var(--grey-photo) 50%,#34373c 100%)}
.intro-text{position:absolute;top:138px;left:95px;width:1010px;text-align:center;color:#e7e8ea;font-weight:300;font-size:34px;line-height:58px}
.intro-text p{margin-bottom:58px}

.banner{top:1456px;height:297px;background:linear-gradient(90deg,#0b2249,#14336a 50%,#0b2249)}
.banner h2{position:absolute;top:76px;width:100%;text-align:center;color:var(--white);font-weight:400;font-size:58px;line-height:66px}

.services{top:1753px;height:2241px;background:var(--white)}
.benefit{position:absolute;left:78px;width:500px}
.benefit h3{color:var(--heading-blue);font-weight:500;font-size:41px;line-height:48px;margin-bottom:12px;max-width:470px}
.benefit h3::before{content:"";display:inline-block;width:14px;height:14px;background:var(--yellow);margin:0 24px 10px 0;vertical-align:middle}
.benefit p{font-size:30px;line-height:45px;font-weight:400}
.b1{top:88px}
.b2{top:780px}
.b3{top:1168px}
.b4{top:1690px}

.offer-col{position:absolute;left:674px;top:78px;width:481px}
.offer-col h2{text-align:center;font-weight:400;font-size:54px;color:#111;margin-bottom:24px}
.card{position:absolute;left:0;width:481px;background:linear-gradient(160deg,#2e3f5a 0%,#1b2b46 55%,#13223b 100%);color:#e5e9f0;padding:36px 30px 0 40px;border-bottom:6px solid #1f5d9d}
.card-head{display:flex;align-items:flex-start;gap:18px;margin-bottom:18px}
.card-head svg{flex:none;width:76px;height:76px}
.card-head h4{font-weight:400;font-size:33px;line-height:37px;color:var(--white)}
.card .desc{font-weight:300;font-size:30px;line-height:45px;margin-bottom:20px}
.card ul{list-style:none}
.card li{font-weight:300;font-size:30px;line-height:45px;padding-left:30px;position:relative}
.card li::before{content:"›";position:absolute;left:0;top:-2px;color:var(--yellow);font-weight:600}
.c1{top:89px;height:548px}
.c2{top:685px;height:649px}
.c3{top:1388px;height:703px}

.tech{top:3994px;height:635px;background:var(--tech-bg)}
.tech h2{position:absolute;top:100px;width:100%;text-align:center;font-weight:400;font-size:54px;color:#111}
.tech-item{position:absolute;transform:translateX(-50%);display:flex;align-items:center;gap:14px;font-weight:500;font-size:30px;color:#3a3f47;white-space:nowrap}
.tech-item i{display:block;width:30px;height:30px;background:var(--blue);border-radius:50%}

.contact{top:4629px;height:578px;background:linear-gradient(180deg,#0e1a33 0%,#1d2a44 60%,#0b1427 100%)}
.contact-card{position:absolute;left:45px;top:68px;width:1110px;height:458px;background:var(--white);border-bottom:8px solid var(--yellow);text-align:center}
.contact-card .brand{position:static;font-size:100px;line-height:1;color:#3c4a5e;margin-top:70px;letter-spacing:1px}
.contact-card address{font-style:normal;font-size:34px;line-height:46px;margin-top:42px;color:#1c1c1c}
.contact-card .phone{font-size:34px;margin-top:34px;color:#1c1c1c}

.site-bar{top:5207px;height:105px;background:var(--blue);color:var(--white);text-align:center;font-size:37px;line-height:105px;font-weight:300}
</style>
</head>
<body>

<header class="hero" role="img" aria-label="Deep blue digital network backdrop with glowing connection lines">
  <div class="brand">Brivolta</div>
  <div class="tagline">Transformation Delivered.</div>
</header>

<section class="intro" role="img" aria-label="Muted photo of a team at work behind the intro text">
  <div class="intro-text">
    <p>Our approach is to give you what you need to get the most from your ERP implementation.</p>
    <p>If you know what that is, we can leverage a resource base of over 200 ERP consultants, both onshore and off, to provide the expertise that will fit seamlessly into your team.</p>
    <p>If you don’t know what you need, we have a process to help you figure that out. Our eight-point assessment starts with strategy and covers the other seven essential elements that ensure implementation success.</p>
  </div>
</section>

<section class="banner">
  <h2>Bringing the Most Value to Your<br>ERP Implementation</h2>
</section>

<section class="services">
  <div class="benefit b1">
    <h3>Emphasis on<br>Process Improvement<br>&amp; Adoption</h3>
    <p>You want to improve processes and ensure adoption. We can help you do both. Brivolta evaluates current processes, identifying process streamlining opportunities along with providing process insight to the ERP implementations. This enables an ERP implementation tailored to your business resulting in increased adoption.</p>
  </div>
  <div class="benefit b2">
    <h3>Bringing Down<br>Costs with the Right<br>Resources</h3>
    <p>If you’re looking for one resource or twenty, working on-site or remote, onshore or off, we can provide them.</p>
  </div>
  <div class="benefit b3">
    <h3>Need to Add<br>Value to Your Current<br>Installation?</h3>
    <p>If you need help to drive the most value from a system already in production, whether it is business intelligence, Flowbench Platform applications, integrations, or new features, we can help.</p>
  </div>
  <div class="benefit b4">
    <h3>Not Sure What<br>You Need?</h3>
    <p>If you sense something is wrong with your implementation but don’t know what it is, we can help. Our eight-point assessment starts with strategy and continues with the seven things that ensure success.</p>
  </div>

  <div class="offer-col">
    <h2>What We Do</h2>

    <div class="card c1">
      <div class="card-head">
        <svg viewBox="0 0 76 76" fill="none" stroke="#f5c518" stroke-width="3"><rect x="4" y="22" width="46" height="46" rx="3"/><path d="M12 56h30M12 46h16M12 36h22"/><circle cx="58" cy="18" r="9"/><circle cx="58" cy="18" r="3"/><path d="M58 4v5M58 27v5M44 18h5M67 18h5"/></svg>
        <h4>ERP<br>Implementations</h4>
      </div>
      <p class="desc">Select and implement the right ERP platform for your needs and objectives</p>
      <ul>
        <li>Start to Finish Implementations</li>
        <li>Project Turnarounds</li>
        <li>Hard to Find Resources</li>
        <li>Value Add Solutions</li>
      </ul>
    </div>

    <div class="card c2">
      <div class="card-head">
        <svg viewBox="0 0 76 76" fill="none" stroke="#f5c518" stroke-width="3"><circle cx="30" cy="24" r="10"/><path d="M10 66c0-14 9-24 20-24s20 10 20 24"/><path d="M46 20l22-14M60 6h8v8"/></svg>
        <h4>ERP Leadership<br>&amp; Staffing</h4>
      </div>
      <p class="desc">Secure top match talent from interim CIOs to software engineers and project managers</p>
      <ul>
        <li>Strategy Focused Leadership and Expertise</li>
        <li>Right-sized for Your Business</li>
        <li>Maximize ROI</li>
        <li>Lead from Experience</li>
      </ul>
    </div>

    <div class="card c3">
      <div class="card-head">
        <svg viewBox="0 0 76 76" fill="none" stroke="#f5c518" stroke-width="3"><circle cx="38" cy="38" r="26"/><ellipse cx="38" cy="38" rx="11" ry="26"/><path d="M12 38h52M16 24h44M16 52h44"/><path d="M2 38h6M68 38h6"/></svg>
        <h4>ERP<br>Transformation<br>&amp; Strategy</h4>
      </div>
      <p class="desc">Define and execute your transformation strategy and clarify technologies to make it real.</p>
      <ul>
        <li>Strategy and Innovation</li>
        <li>Digital and Technology Prioritization &amp; Roadmap</li>
        <li>Executive Coaching</li>
        <li>Process Adoption &amp; Optimization</li>
      </ul>
    </div>
  </div>
</section>

<section class="tech">
  <h2>Technologies</h2>
  <div class="tech-item" style="left:268px;top:290px"><i></i>Corvance 365</div>
  <div class="tech-item" style="left:567px;top:290px">Ledgerly</div>
  <div class="tech-item" style="left:790px;top:290px">Aurelo Cloud</div>
  <div class="tech-item" style="left:1037px;top:290px">Framewise</div>
  <div class="tech-item" style="left:262px;top:446px"><i></i>Flowbench Platform</div>
  <div class="tech-item" style="left:522px;top:446px">Insightra</div>
  <div class="tech-item" style="left:790px;top:446px">Skyvault</div>
  <div class="tech-item" style="left:1030px;top:446px"><i></i>Relata</div>
</section>

<footer class="contact" role="img" aria-label="Night city skyline with scattered lights behind the contact card">
  <div class="contact-card">
    <div class="brand">Brivolta</div>
    <address>418 Larkmoor Plaza, Suite 212,<br>Eastbrook, MN, 55990</address>
    <div class="phone">(555) 014-2876</div>
  </div>
</footer>

<section class="site-bar">brivoltaconsulting.com</section>

</body>
</html>
```